Covid19 Poster for workplaces

Create a poster on how to protect yourself from Corona virus at work.
We are a Staffwell Works company. We have just re-branded so we need to fit in with our brand. We like clean and fresh, slightly amusing is ok if it will draw attention but it's an important topic. A4 and A3 please.

Content:

Headline: Lower the risk of COVID 19 in the workplace.

BE WELL

Bring your own cup - don’t share cups and food.
Elbow tap instead of handshakes and kisses
Wash your hands often - with soap.
Elbow or tissues when you cough or sneeze then straight in the bin
Leave your face alone after touching shared surfaces
Leave your bugs at home if you’re feeling unwell.

Call health line if you have a cough, a high temperature and shortness of breath. 0800 472 9160

Based on recommendations from ZPK and QLN

Target Market(s)

Employees - so anyone

Other font styles liked:
• Use the closest font to the brand documents

Requirements
Should not have
• Clip art

```html
<!DOCTYPE html>
<html lang="en">
<head>
<meta charset="utf-8">
<title>Lower the risk of COVID 19 in the workplace</title>
<link rel="stylesheet" href="https://fonts.googleapis.com/css2?family=Inter:wght@600;700;800&display=swap">
<style>
  :root {
    --teal: #1aa6b3;
    --teal-deep: #13909c;
    --white: #ffffff;
    --ink: #231f20;
    --rule: rgba(255,255,255,0.9);
  }
  * { box-sizing: border-box; margin: 0; padding: 0; }
  html, body { width: 849px; height: 1200px; overflow: hidden; background: var(--teal); }
  .poster {
    position: relative; width: 849px; height: 1200px;
    background: var(--teal); color: var(--white);
    font-family: "Inter", Helvetica, Arial, sans-serif;
  }
  .headline {
    position: absolute; left: 68px; top: 82px; width: 600px;
    font-size: 69px; font-weight: 700; line-height: 68px; letter-spacing: -2.2px;
  }
  .rule { position: absolute; height: 1px; background: var(--rule); width: 339px; }
  .rule--left { left: 72px; }
  .rule--right { left: 437px; }
  .campaign {
    position: absolute; left: 70px; top: 380px;
    font-size: 96px; font-weight: 700; letter-spacing: -3px; line-height: 110px;
  }
  .tip { position: absolute; display: flex; align-items: center; }
  .tip__icon {
    flex: none; width: 78px; height: 78px; border-radius: 8px;
    background: var(--teal-deep);
  }
  .tip__text {
    font-size: 19.5px; font-weight: 700; line-height: 22.5px; letter-spacing: -0.2px;
    margin-left: 14px; white-space: nowrap;
  }
  .tip--left { left: 73px; }
  .tip--right { left: 451px; }
  .tip--right .tip__icon { width: 68px; }
  .tip--right .tip__text { margin-left: 18px; }
  .call {
    position: absolute; left: 72px; top: 932px; width: 740px;
    font-size: 27.2px; font-weight: 700; line-height: 38px; letter-spacing: -0.4px;
  }
  .based {
    position: absolute; left: 72px; top: 1062px;
    font-size: 19px; font-weight: 700; letter-spacing: -0.2px;
  }
  .partner {
    position: absolute; top: 1094px; display: flex; align-items: center;
    font-weight: 700; color: var(--white);
  }
  .partner--qln {
    left: 73px; width: 139px; height: 43px; border: 1px solid var(--white);
    justify-content: center; font-size: 22px; letter-spacing: 1px;
  }
  .partner--zpk { left: 234px; height: 54px; font-size: 26px; }
  .partner__dot {
    width: 42px; height: 42px; border-radius: 50%; border: 2px solid var(--white);
    margin-right: 12px;
  }
  .client {
    position: absolute; left: 537px; top: 1100px; display: flex; align-items: center;
  }
  .client__mark { width: 56px; height: 56px; border-radius: 50%; background: var(--white); margin-right: 18px; }
  .client__name {
    color: var(--ink); font-size: 27px; font-weight: 800; line-height: 26px; letter-spacing: -0.8px;
  }
</style>
</head>
<body>
<main class="poster">
  <h1 class="headline">Lower the risk of<br>COVID 19 in the<br>workplace!</h1>

  <div class="rule rule--left" style="top:360px"></div>
  <h2 class="campaign">THRIVE</h2>
  <div class="rule rule--left" style="top:511px"></div>
  <div class="rule rule--right" style="top:511px"></div>

  <div class="tip tip--left" style="top:549px">
    <div class="tip__icon" role="img" aria-label="Icon of a steaming cup"></div>
    <p class="tip__text">Bring your own cup - don’t<br>share cups and food.</p>
  </div>
  <div class="tip tip--left" style="top:669px">
    <div class="tip__icon" role="img" aria-label="Icon of a handshake crossed out"></div>
    <p class="tip__text">Elbow tap instead of<br>handshakes and kisses</p>
  </div>
  <div class="tip tip--left" style="top:790px">
    <div class="tip__icon" role="img" aria-label="Icon of hands being washed with water drops"></div>
    <p class="tip__text">Wash your hands<br>often - with soap</p>
  </div>

  <div class="tip tip--right" style="top:550px">
    <div class="tip__icon" role="img" aria-label="Icon of a person sneezing into their elbow"></div>
    <p class="tip__text">Elbow or tissues when<br>you cough or sneeze then<br>straight in the bin</p>
  </div>
  <div class="tip tip--right" style="top:669px">
    <div class="tip__icon" role="img" aria-label="Icon of a person touching their face"></div>
    <p class="tip__text">Leave your face alone<br>after touching shared<br>surfaces</p>
  </div>
  <div class="tip tip--right" style="top:790px">
    <div class="tip__icon" role="img" aria-label="Icon of a head with a thermometer"></div>
    <p class="tip__text">Leave your bugs at home<br>if you’re feeling unwell</p>
  </div>

  <p class="call">Call health line if you have a cough, a high temperature<br>and shortness of breath. 0800 472 9160</p>

  <div class="rule rule--left" style="top:1033px"></div>
  <div class="rule rule--right" style="top:1033px"></div>

  <p class="based">Based on recommendations by</p>
  <div class="partner partner--qln">QLN</div>
  <div class="partner partner--zpk"><span class="partner__dot"></span>ZPK</div>

  <div class="client">
    <span class="client__mark"></span>
    <span class="client__name">Staffwell<br>Works</span>
  </div>
</main>
</body>
</html>
```